Personal Training

The name of my company is Heron Vitality. I am looking for a design that will feature the 8 components I am utilizing in my workouts (strength, flexibility, agility, core, power, balance, cardiovacular, speed) and represent the spider. It is not essesstial to have a spider for my logo but would be nice. If a spider is used please do not use a logo like Crowlord, a tarantula, or anything scary involving a spider (I have female clients who would get scared) lol
If you need me to provide more information please let me know. Feel free to check my website for ideas but ignore the pictures on my site as those are not pictures of me or clients
Thank you in advance!

Industry/Entity Type

Fitness

Contact Information for Business Card

Dale Presky
Company Name: Heron Vitality
Tag line: 8 components to a better you
Website: hervit7.example
Email: dale@hervit7.example
Cell: 555-413-2086

KPTB Certified Personal Trainer
CPR AED Northern Pulse Council
B.A. Exercise Physiology W.L.M., 2004

```html
<!DOCTYPE html>
<html lang="en">
<head>
<meta charset="utf-8">
<title>Heron Vitality — Business Card</title>
<link href="https://fonts.googleapis.com/css2?family=Open+Sans:wght@400;600;800&family=Oswald:wght@500&family=Michroma&display=swap" rel="stylesheet">
<style>
  :root {
    --brand-red: #d9151b;
    --ink: #1a1a1a;
    --band: #0d0d0d;
    --card: #ffffff;
    --backdrop: #e9e6e4;
    --muted: #2b2b2b;
  }
  * { margin: 0; padding: 0; box-sizing: border-box; }
  html, body { width: 1200px; height: 800px; overflow: hidden; }
  body {
    background: var(--backdrop);
    font-family: "Open Sans", Arial, sans-serif;
    position: relative;
  }
  .business-card {
    position: absolute;
    left: 150px; top: 143px;
    width: 900px; height: 514px;
    background: var(--card);
    box-shadow: 0 10px 30px rgba(0,0,0,.18);
    overflow: hidden;
  }
  .brand {
    position: absolute;
    left: 60px; top: 110px;
    display: flex; align-items: center; gap: 28px;
  }
  .brand-square {
    width: 150px; height: 150px;
    border-radius: 22px;
    background: var(--brand-red);
    border: 5px solid var(--ink);
  }
  .brand-name {
    font-weight: 800;
    font-size: 62px;
    line-height: 1;
    color: var(--brand-red);
    letter-spacing: 1px;
  }
  .brand-tagline {
    margin-top: 12px;
    font-family: "Michroma", Arial, sans-serif;
    font-size: 17px;
    letter-spacing: 5px;
    text-transform: uppercase;
    color: var(--ink);
  }
  .trainer {
    position: absolute;
    left: 110px; top: 290px;
  }
  .trainer-name {
    font-weight: 800;
    font-size: 26px;
    color: var(--brand-red);
    line-height: 1.1;
  }
  .credentials {
    list-style: none;
    font-size: 17px;
    font-weight: 400;
    color: var(--muted);
    line-height: 1.25;
    padding-left: 16px;
  }
  .contacts {
    list-style: none;
    position: absolute;
    left: 140px; top: 378px;
  }
  .contacts li {
    display: flex; align-items: center; gap: 8px;
    font-size: 26px;
    font-weight: 600;
    color: var(--ink);
    line-height: 1.22;
  }
  .contacts svg { width: 22px; height: 22px; flex: none; }
  .accent-line {
    position: absolute; left: 0; right: 0; bottom: 64px;
    height: 5px; background: var(--brand-red);
  }
  .components-band {
    position: absolute; left: 0; right: 0; bottom: 0;
    height: 64px;
    background: var(--band);
    display: flex; align-items: center; justify-content: center;
    font-family: "Oswald", Arial, sans-serif;
    font-weight: 500;
    font-size: 19px;
    letter-spacing: 3.5px;
    color: #fff;
    text-transform: uppercase;
  }
</style>
</head>
<body>
  <article class="business-card">
    <header class="brand">
      <div class="brand-square"></div>
      <div class="brand-text">
        <h1 class="brand-name">Heron Vitality</h1>
        <p class="brand-tagline">8 components to a better you</p>
      </div>
    </header>

    <section class="trainer">
      <h2 class="trainer-name">Dale Presky</h2>
      <ul class="credentials">
        <li>KPTB Certified Personal Trainer</li>
        <li>CPR AED Northern Pulse Council</li>
        <li>B.A. Exercise Physiology W.L.M., 2004</li>
      </ul>
    </section>

    <ul class="contacts">
      <li>
        <svg viewBox="0 0 24 24" aria-hidden="true"><rect x="6" y="1.5" width="12" height="21" rx="2" fill="none" stroke="#d9151b" stroke-width="2"/><rect x="8.5" y="4.5" width="7" height="9" fill="#d9151b"/><circle cx="12" cy="18.5" r="1.4" fill="#d9151b"/></svg>
        555-413-2086
      </li>
      <li>
        <svg viewBox="0 0 24 24" aria-hidden="true"><circle cx="12" cy="12" r="10" fill="#d9151b"/><g fill="none" stroke="#fff" stroke-width="1.4"><ellipse cx="12" cy="12" rx="4.5" ry="9.5"/><path d="M2.5 12h19M4 7h16M4 17h16M12 2v20"/></g></svg>
        hervit7.example
      </li>
      <li>
        <svg viewBox="0 0 24 24" aria-hidden="true"><circle cx="12" cy="12" r="11" fill="#d9151b"/><rect x="5" y="7.5" width="14" height="9.5" fill="#fff"/><path d="M5 7.5l7 5.5 7-5.5" fill="none" stroke="#d9151b" stroke-width="1.4"/></svg>
        dale@hervit7.example
      </li>
    </ul>

    <div class="accent-line"></div>
    <footer class="components-band">Strength, Flexibility, Agility, Core, Power, Balance, Cardiovacular, Speed</footer>
  </article>
</body>
</html>
```